corvane business cards

Hey design gurus!
I'm after a clean, modern, stylish business card for my about to be launched company.
I've uploaded the logos for my company "Corvane Electrical Solutions"
and also the brightway electricians logo to whom i am associated.

```html
<!DOCTYPE html>
<html lang="en">
<head>
<meta charset="utf-8">
<title>Corvane Electrical Solutions – Business Cards</title>
<link href="https://fonts.googleapis.com/css2?family=Open+Sans:wght@400;600;700;800&display=swap" rel="stylesheet">
<style>
  :root{
    --stage:#232323;
    --card-dark:#1f1f24;
    --card-dark-text:#2c2c32;
    --card-light:#ffffff;
    --brand-blue:#0b76c1;
    --ink:#111111;
    --badge-red:#a5473a;
    --badge-navy:#1e2a4a;
  }
  *{box-sizing:border-box;margin:0;padding:0}
  html,body{width:1200px;height:780px;overflow:hidden;background:var(--stage)}
  body{font-family:"Open Sans",sans-serif;display:flex;align-items:center;justify-content:center;gap:40px}

  .card{position:relative;width:540px;height:309px;border-radius:22px;overflow:hidden;border:4px solid var(--brand-blue);box-shadow:0 12px 30px rgba(0,0,0,.55)}

  /* back */
  .card--back{background:var(--card-dark);display:flex;align-items:center;justify-content:center;gap:16px}
  .back-mark{width:56px;height:56px;border-radius:50%;border:5px solid var(--card-dark-text)}
  .back-name{color:var(--card-dark-text);font-weight:800;line-height:1;text-transform:uppercase}
  .back-name .line1{display:block;font-size:44px;letter-spacing:1px}
  .back-name .line2{display:block;font-size:14px;letter-spacing:3px;margin-top:4px}

  /* front */
  .card--front{background:var(--card-light)}
  .front-brand{position:absolute;left:28px;top:70px;width:210px;display:flex;flex-direction:column;align-items:center;gap:12px}
  .front-brand .mark{width:70px;height:70px;border-radius:50%;border:8px solid var(--brand-blue)}
  .front-brand .name{font-weight:800;font-size:30px;color:var(--ink);letter-spacing:.5px}
  .divider{position:absolute;left:258px;top:40px;width:2px;height:170px;background:var(--ink)}
  .contact{position:absolute;left:280px;top:38px;color:var(--ink)}
  .person{font-weight:700;font-size:24px;line-height:1.1}
  .person .first{color:var(--brand-blue)}
  .role{font-weight:600;font-size:13px;margin-top:2px}
  .address{font-size:12.5px;line-height:1.35;margin-top:14px}
  .links{list-style:none;margin-top:14px;font-size:12.5px;line-height:1.55}
  .links li{display:flex;align-items:center;gap:8px}
  .links svg{width:13px;height:13px;flex:none}
  .band{position:absolute;height:14px}
  .band--blue{left:0;width:300px;top:262px;background:var(--brand-blue)}
  .band--black{right:0;width:150px;top:240px;background:var(--ink)}
  .partner-badge{position:absolute;left:306px;top:232px;width:76px;height:32px;border:2px solid var(--badge-red);border-radius:5px;background:#fff;display:flex;align-items:center;padding-left:5px}
  .partner-badge span{width:18px;height:18px;background:var(--badge-navy);border-radius:3px}
</style>
</head>
<body>
  <section class="card card--back" aria-label="Card back">
    <div class="back-mark"></div>
    <div class="back-name"><span class="line1">Corvane</span><span class="line2">Electrical Solutions</span></div>
  </section>

  <section class="card card--front" aria-label="Card front">
    <div class="front-brand">
      <div class="mark"></div>
      <div class="name">CORVANE</div>
    </div>
    <div class="divider"></div>
    <div class="contact">
      <p class="person"><span class="first">Mirela</span> Haskova</p>
      <p class="role">Managing Director</p>
      <p class="address">1840 Larkspur Ave. Suite<br>310 Dunmore, TX 75410</p>
      <ul class="links">
        <li><svg viewBox="0 0 16 16"><path fill="#0b76c1" d="M3.6 1.5l2.3 2.6-1.4 1.6c.9 2 2.6 3.7 4.6 4.6l1.6-1.4 2.6 2.3-1.3 2.3C6.5 13.1 2.9 9.5 1.3 3z"/></svg>(555) 214-6630</li>
        <li><svg viewBox="0 0 16 16"><rect x="1" y="3" width="14" height="10" rx="1" fill="#0b76c1"/><path d="M1.5 3.5L8 9l6.5-5.5" stroke="#fff" stroke-width="1.3" fill="none"/></svg>info@corvane-electric.com</li>
        <li><svg viewBox="0 0 16 16"><circle cx="8" cy="8" r="7" fill="#0b76c1"/><path d="M1 8h14M8 1c-3 3.5-3 10.5 0 14M8 1c3 3.5 3 10.5 0 14" stroke="#fff" stroke-width="1" fill="none"/></svg>www.corvane-electric.com</li>
      </ul>
    </div>
    <div class="band band--blue"></div>
    <div class="partner-badge" aria-label="Partner badge"><span></span></div>
    <div class="band band--black"></div>
  </section>
</body>
</html>
```